Веб-сайт для lesnoyprival.ru
Название сайта (домена, или проекта)
lesnoyprival.ru
Нужен редизайн сайта сети мини-отелей Леснопривал (lesnoyprival.ru).
Для конкурса нужны макеты следующих страниц:
1) Главная
2) Страница отеля
3) Страница бронирования
4) Страница с отзывами
5) Страница с анонсами событий
6) Страница блога
Необходимая структура страниц и сайта в целом - http://inn.tovarisch/wp-content/uploads/2016/03/lesnoyprival.ru_.png
Пример схожей структуры сайта, которая нужна, у дочерней нашей сети inn.tovarisch
Примеры страниц бронирования - http://inn.tovarisch/booking-step-1, http://lesnoyprival.ru/booking
Логотип тоже нужен, но делать по желанию
Тексты брать с сайта lesnoyprival.ru
Адаптивность сайта
Десктопная версия, Версия для планшетов, Версия для телефонов

```html
<!DOCTYPE html>
<html lang="ru">
<head>
<meta charset="utf-8">
<title>Леснопривал — ближайшие номера</title>
<link rel="stylesheet" href="https://fonts.googleapis.com/css2?family=Roboto:wght@300;400;500;700&display=swap">
<style>
  :root {
    --page: #f4f4f4;
    --paper: #ffffff;
    --card: #e8e8e8;
    --accent: #f2cf4a;
    --ink: #2b2b2b;
    --muted: #8d8d8d;
    --line: #cfcfcf;
    --rule: #dedede;
  }
  * { box-sizing: border-box; margin: 0; padding: 0; }
  html, body { width: 1200px; height: 915px; overflow: hidden; }
  body { background: var(--page); font-family: "Roboto", sans-serif; color: var(--ink); position: relative; }

  .topbar { position: absolute; left: 0; top: 0; width: 1200px; height: 44px; background: var(--paper); border-bottom: 1px solid var(--rule); }
  .brand { position: absolute; left: 28px; top: 13px; font-size: 16px; font-weight: 700; }
  .nav { position: absolute; left: 360px; top: 0; display: flex; height: 44px; }
  .nav a { display: block; padding: 0 16px; line-height: 44px; font-size: 11px; color: var(--ink); text-decoration: none; }
  .nav a.is-active { background: var(--accent); height: 30px; line-height: 30px; margin-top: 7px; }

  .menu-icon { position: absolute; width: 16px; height: 12px; border-top: 2px solid var(--ink); border-bottom: 2px solid var(--ink); }
  .menu-icon::after { content: ""; position: absolute; left: 0; top: 3px; width: 16px; height: 2px; background: var(--ink); }

  .rooms-head { position: absolute; left: 52px; top: 70px; font-size: 12px; font-weight: 700; letter-spacing: .04em; }
  .rooms-head .menu-icon { left: 0; top: 0; }
  .rooms-head .title { position: absolute; left: 30px; top: 0; white-space: nowrap; }
  .rooms-head .switch { position: absolute; left: 250px; top: 0; white-space: nowrap; color: var(--muted); font-weight: 500; }

  .call-box { position: absolute; left: 870px; top: 52px; width: 230px; height: 64px; background: var(--accent); text-align: center; padding-top: 14px; }
  .call-box small, .call-note small { display: block; font-size: 9px; color: #6b5a1a; }
  .call-box strong { display: block; font-size: 19px; font-weight: 700; margin-top: 4px; }

  .room-title { position: absolute; top: 126px; font-size: 10px; font-weight: 700; display: flex; align-items: center; gap: 6px; }
  .room-title .dot { width: 10px; height: 10px; border-radius: 50%; border: 2px solid var(--ink); }
  .room-title .stars { color: var(--muted); letter-spacing: 2px; font-weight: 400; margin-left: 36px; }

  .room-card { position: absolute; top: 152px; width: 232px; height: 310px; background: var(--card); }
  .room-card.is-featured { background: var(--accent); }
  .room-card svg { position: absolute; left: 56px; top: 56px; }
  .timer { position: absolute; left: 0; top: 108px; width: 232px; text-align: center; }
  .timer small { display: block; font-size: 9px; color: var(--muted); }
  .is-featured .timer small { color: #6b5a1a; }
  .timer strong { display: block; font-size: 30px; font-weight: 500; }
  .card-actions { position: absolute; left: 18px; bottom: 14px; right: 18px; display: flex; justify-content: space-between; }
  .card-actions span { background: var(--paper); font-size: 9px; padding: 5px 8px; }

  .text-lines { position: absolute; top: 488px; width: 200px; }
  .text-lines i { display: block; height: 2px; background: var(--line); margin-bottom: 9px; }

  .price-row { position: absolute; top: 590px; display: flex; align-items: center; gap: 16px; }
  .price { font-size: 18px; font-weight: 500; }
  .price small { font-size: 10px; color: var(--muted); font-weight: 400; }
  .order { font-size: 10px; padding: 7px 12px; border: 1px solid var(--line); background: var(--paper); }
  .order.is-featured { background: var(--accent); border-color: var(--accent); }

  .about { position: absolute; left: 0; top: 660px; width: 1200px; height: 255px; background: var(--paper); border-top: 1px solid var(--rule); }
  .about-head { position: absolute; left: 52px; top: 40px; font-size: 12px; font-weight: 700; letter-spacing: .04em; }
  .about-head .menu-icon { left: 0; top: 0; }
  .about-head span { position: absolute; left: 30px; top: 0; white-space: nowrap; }
  .about h1 { position: absolute; left: 56px; top: 96px; font-size: 15px; font-weight: 500; }
  .about p { position: absolute; left: 56px; top: 128px; width: 620px; font-size: 11px; line-height: 1.7; color: var(--muted); font-weight: 300; }
  .city-art { position: absolute; left: 700px; top: 12px; width: 220px; height: 70px; background: linear-gradient(180deg, #fafafa, #ececec); }
  .call-note { position: absolute; left: 930px; top: 30px; text-align: center; width: 170px; }
  .call-note small { color: var(--muted); }
  .call-note strong { display: block; font-size: 15px; font-weight: 700; margin-top: 3px; }
</style>
</head>
<body>
  <header class="topbar">
    <div class="brand">Леснопривал</div>
    <nav class="nav">
      <a class="is-active" href="#">Бронирование</a>
      <a href="#">О компании</a>
      <a href="#">Программа лояльности</a>
      <a href="#">Акции и мероприятия</a>
      <a href="#">Новости</a>
      <a href="#">Санкт-Петербург</a>
    </nav>
  </header>

  <div class="rooms-head">
    <div class="menu-icon"></div>
    <div class="title">БЛИЖАЙШИЕ К ВАМ НОМЕРА</div>
    <div class="switch">ВЫБРАТЬ ПО ВРЕМЕНИ</div>
  </div>

  <div class="call-box"><small>Бесплатный звонок по России</small><strong>8 800 505 21 21</strong></div>

  <div class="room-title" style="left:232px"><span class="dot"></span>ЛИТЕЙНЫЙ 12<span class="stars">★★★★</span></div>
  <div class="room-title" style="left:496px"><span class="dot"></span>САДОВАЯ 18<span class="stars">★★★★</span></div>
  <div class="room-title" style="left:760px"><span class="dot"></span>МОРСКАЯ 40<span class="stars">★★★★</span></div>

  <article class="room-card" style="left:232px">
    <svg width="120" height="120" viewBox="0 0 120 120"><circle cx="60" cy="60" r="54" fill="none" stroke="#cfcfcf" stroke-width="2"/><circle cx="60" cy="60" r="54" fill="none" stroke="#2b2b2b" stroke-width="5" stroke-dasharray="60 400" transform="rotate(-90 60 60)"/></svg>
    <div class="timer"><small>До номера</small><strong>0:18</strong></div>
    <div class="card-actions"><span>На карте</span><span>Маршрут</span></div>
  </article>
  <article class="room-card is-featured" style="left:496px">
    <svg width="120" height="120" viewBox="0 0 120 120"><circle cx="60" cy="60" r="54" fill="none" stroke="#ffffff" stroke-width="2"/><circle cx="60" cy="60" r="54" fill="none" stroke="#2b2b2b" stroke-width="5" stroke-dasharray="200 400" transform="rotate(-90 60 60)"/></svg>
    <div class="timer"><small>До номера</small><strong>0:35</strong></div>
    <div class="card-actions"><span>На карте</span><span>Маршрут</span></div>
  </article>
  <article class="room-card" style="left:760px">
    <svg width="120" height="120" viewBox="0 0 120 120"><circle cx="60" cy="60" r="54" fill="none" stroke="#2b2b2b" stroke-width="5"/></svg>
    <div class="timer"><small>До номера</small><strong>1:18</strong></div>
    <div class="card-actions"><span>На карте</span><span>Маршрут</span></div>
  </article>

  <div class="text-lines" style="left:248px"><i></i><i></i><i></i><i></i><i></i><i></i><i></i></div>
  <div class="text-lines" style="left:512px"><i></i><i></i><i></i><i></i><i></i><i></i><i></i></div>
  <div class="text-lines" style="left:776px"><i></i><i></i><i></i><i></i><i></i><i></i><i></i></div>

  <div class="price-row" style="left:248px"><span class="price">1500 <small>₽ /сутки</small></span><span class="order">Заказать</span></div>
  <div class="price-row" style="left:512px"><span class="price">3800 <small>₽ /сутки</small></span><span class="order is-featured">Заказать</span></div>
  <div class="price-row" style="left:776px"><span class="price">6900 <small>₽ /сутки</small></span><span class="order">Заказать</span></div>

  <section class="about">
    <div class="about-head"><div class="menu-icon"></div><span>ОБ ОТЕЛЕ</span></div>
    <div class="city-art" role="img" aria-label="Лёгкий контурный рисунок городских крыш"></div>
    <div class="call-note"><small>Бесплатный звонок по России</small><strong>8 800 505 21 21</strong></div>
    <h1>«Леснопривал» — недорогие отели Санкт-Петербурга</h1>
    <p>Уютные номера в центре города, рядом с метро и главными улицами. Выберите ближайший отель и забронируйте номер онлайн за пару минут.</p>
  </section>
</body>
</html>
```